Flyer für Stadtverwaltung
Zielgruppe
Wir sind die Stadtverwaltung der Stadt Wermelskirchen,
unsere Zielgruppe sind Schüler/innen, welche demnächst ihren Abschluss machen und Interesse an einer Ausbildung oder einem dualen Studium haben.
Aber auch alle weiteren Personengruppen, die sich für eine Ausbildung oder ein duales Studium interessieren.
Aufgabenstellung
Sehr geehrtes Team von Kreavolo,
unser Flyer soll hauptsächlich Schüler/innen ansprechen,
die in näherer Zukunft ihren Abschluss machen und Interesse an einer Ausbildung oder einem dualen Studium haben.
Darf sich jedoch an jede/n richten, der/die Interesse an einer Ausbildung oder einem dualen Studium hat.
Der Flyer soll DIN A5 Format haben, ob quer oder hoch ist den Designer/innen überlassen, wir sind offen für Ideen und Vorschläge.
Was auf den Flyer muss:
1. Die folgenden Ausbildungsberufe (In exakt der vorgegebenen Schreibweise)
> unsere Ausschreibungen richten sich an Personen jeglichen Geschlechts (m/w/d) sowie an Personen mit einer Schwerbehinderung (dies sollte in irgendeiner Form auf dem Flyer deutlich werden)
- Bachelor- Studiengang Kommunaler Verwaltungsdienst
- Bachelor- Studiengang Verwaltungsinformatik
- Verwaltungsfachangestellte/r
- Straßenwärter/in
- Fachangestellte/r für Medien- und Informationsdienste
- Fachangestellte/r für Bäderbetriebe
- Fachinformatiker/in in der Fachrichtung Systemintegration
- Brandmeisteranwärter/in
- Ausbildung zum/zur Notfallsanitäter/in
- Elektroniker/in für Betriebstechnik
- PIA- Ausbildung
2. Die beigefügten Fotos
- Die Fotos dürfen gerne ergänzt, ersetzt oder vollständig weggelassen werden
- Gerne dürfen eigene Designs, Grafiken, Bilder oder sonstige Formen der Darstellung verwendet werden die der Gestaltung des Flyers dienlich sind. (Wir freuen uns auf Kreative Ideen)
- Eine Orientierung am Stil der Fotos ist ebenso nicht notwendig
Der Flyer soll die Vielfalt an beruflichen Optionen widerspiegeln, die es bei der Stadt Wermelskirchen gibt.
Zudem soll die Stadt Wermelskirchen als offener und toleranter Arbeitgeber präsentiert werden, dem seine Angestellten am Herzen liegen.
Ideen und Anregungen für den Flyer:
Die Möglichkeit:
- eine Beamtenlaufbahn einzuschlagen
- draußen zu arbeiten

```html
<!DOCTYPE html>
<html lang="de">
<head>
<meta charset="utf-8">
<title>Karrieremöglichkeiten – Flyer</title>
<link rel="stylesheet" href="https://fonts.googleapis.com/css2?family=Poppins:ital,wght@0,400;0,700;1,400;1,700&display=swap">
<style>
  :root {
    --page-bg: #c9c9c9;
    --paper: #ffffff;
    --ink: #1f1f1f;
    --ink-soft: #3a3a3a;
    --note-grey: #444444;
    --banner-dark: #141414;
    --banner-mid: #3a3a3a;
    --accent-yellow: #f2ea3a;
    --photo-light: #d6d7da;
    --photo-mid: #9a9ca0;
    --photo-dark: #3a3b3e;
  }
  * { margin: 0; padding: 0; box-sizing: border-box; }
  html, body {
    width: 1200px;
    height: 1200px;
    overflow: hidden;
    background: var(--page-bg);
    font-family: "Poppins", sans-serif;
  }
  .flyer {
    position: absolute;
    left: 212px;
    top: 50px;
    width: 776px;
    height: 1100px;
    background: linear-gradient(180deg, #f6f6f6 0%, var(--paper) 18%, var(--paper) 100%);
    overflow: hidden;
    box-shadow: 0 4px 18px rgba(0,0,0,0.12);
  }
  .inclusion-note {
    position: absolute;
    left: 59px;
    top: 63px;
    width: 640px;
    font-style: italic;
    font-size: 16.5px;
    line-height: 1.15;
    color: var(--note-grey);
  }
  .note-rule {
    position: absolute;
    left: 59px;
    top: 122px;
    width: 640px;
    height: 3px;
    background: linear-gradient(90deg, #2a2a2a 0%, #777 50%, rgba(150,150,150,0) 100%);
  }
  .section-banner {
    position: absolute;
    left: 0;
    top: 159px;
    width: 452px;
    height: 48px;
    background: linear-gradient(90deg, var(--banner-dark) 0%, var(--banner-mid) 100%);
    display: flex;
    align-items: center;
    padding-left: 55px;
  }
  .section-banner h1 {
    font-weight: 700;
    font-size: 32.5px;
    color: var(--accent-yellow);
    letter-spacing: -0.2px;
    white-space: nowrap;
  }
  .career-list {
    position: absolute;
    left: 55px;
    top: 228px;
    list-style: none;
    font-size: 16px;
    line-height: 27.8px;
    color: var(--ink);
  }
  .career-list li::before {
    content: "— ";
    color: var(--ink-soft);
  }
  .tagline-banner {
    position: absolute;
    left: 0;
    top: 560px;
    width: 516px;
    height: 31px;
    background: linear-gradient(90deg, var(--banner-dark) 0%, var(--banner-mid) 100%);
    display: flex;
    align-items: center;
    padding-left: 57px;
  }
  .tagline-banner p {
    font-weight: 700;
    font-style: italic;
    font-size: 18.7px;
    color: var(--accent-yellow);
    white-space: nowrap;
  }
  .contact-row {
    position: absolute;
    top: 615px;
    left: 0;
    width: 100%;
    font-style: italic;
    font-size: 19px;
    color: var(--ink);
  }
  .contact-row span { position: absolute; white-space: nowrap; }
  .contact-mobile { left: 59px; }
  .contact-email { left: 366px; }
  .contact-address { left: 611px; }
  .hero-photo {
    position: absolute;
    left: 0;
    top: 668px;
    width: 100%;
    height: 432px;
    background:
      linear-gradient(180deg, rgba(255,255,255,1) 0%, rgba(255,255,255,0) 18%),
      linear-gradient(180deg, var(--photo-light) 0%, var(--photo-mid) 55%, var(--photo-dark) 100%);
  }
</style>
</head>
<body>
  <article class="flyer">
    <p class="inclusion-note">**unsere Ausschreibungen richten sich an Personen jeglichen Geschlechts (m/f/d) sowie an Personen mit einer Schwerbehinderung</p>
    <div class="note-rule"></div>

    <header class="section-banner">
      <h1>Karrieremöglichkeiten.</h1>
    </header>

    <ul class="career-list">
      <li>Bachelor- Studiengang Kommunaler Verwaltungsdienst</li>
      <li>Bachelor- Studiengang Verwaltungsinformatik</li>
      <li>Verwaltungsfachangestellte/r</li>
      <li>Straßenwärter/in</li>
      <li>Fachangestellte/r für Medien- und Informationsdienste</li>
      <li>Fachangestellte/r für Bäderbetriebe</li>
      <li>Fachinformatiker/in in der Fachrichtung Systemintegration</li>
      <li>Brandmeisteranwärter/in</li>
      <li>Ausbildung zum/zur Notfallsanitäter/in</li>
      <li>Elektroniker/in für Betriebstechnik</li>
      <li>PIA- Ausbildung</li>
    </ul>

    <div class="tagline-banner">
      <p>Buchen Sie Ihren 30-tägigen Urlaub bei uns.</p>
    </div>

    <div class="contact-row">
      <span class="contact-mobile">Mobile number</span>
      <span class="contact-email">Email</span>
      <span class="contact-address">Address</span>
    </div>

    <div class="hero-photo" role="img" aria-label="Foto: Mitarbeiterin in Warnschutzkleidung vor einem städtischen Nutzfahrzeug"></div>
  </article>
</body>
</html>
```